Online media outlet needs a blog and logo

A new online blog platform is being established in the UK. The blog will be very similar in layout to www.lumvero.co. It will need to have a main story slider showing three slides and block tiles beneath the slider for additional tiles.

The blog platform will be called 'Brisket Lantern' and will also need a professional looking logo design for the name.

The website should be designed in Word Press.

Industry/Entity Type

Media

Logo Text

Brisket Lantern

Coding

Coded - Design and coding required

Number of Pages Required

3 page

Font styles to use
Other font styles liked:
• Helvetica

Requirements
Must have
• A slider showing three slides. Be similar to Lum V (see previous comment). Be Word Press compatible.

```html
<!DOCTYPE html>
<html lang="en">
<head>
<meta charset="utf-8">
<title>Brisket Lantern</title>
<link rel="stylesheet" href="https://fonts.googleapis.com/css2?family=Montserrat:wght@400;600;700;800&display=swap">
<style>
:root{
  --navy:#0b2a5b;
  --navy-deep:#072048;
  --yellow:#fde425;
  --white:#ffffff;
  --grey-bg:#efefef;
  --caption:rgba(205,210,218,.88);
  --ink:#1d2a44;
}
*{margin:0;padding:0;box-sizing:border-box}
html,body{width:1200px;height:1120px;overflow:hidden;background:var(--white);font-family:"Montserrat",Helvetica,Arial,sans-serif;color:var(--ink)}
.page{position:absolute;left:418px;top:0;width:364px;height:1120px;background:var(--white)}
.abs{position:absolute}

/* header */
.site-header{left:0;top:0;width:364px;height:26px;background:var(--navy)}
.social-dots{left:13px;top:9px;display:flex;gap:2px}
.social-dots span{width:8px;height:8px;border-radius:50%;background:var(--yellow)}
.brand{left:0;width:364px;top:7px;text-align:center;font-weight:800;font-size:10px;letter-spacing:.5px;color:var(--yellow)}
.menu-icon{left:340px;top:9px;width:9px}
.menu-icon i{display:block;height:1.4px;background:var(--white);margin-bottom:1.6px}

/* hero */
.hero{left:0;top:26px;width:364px;height:226px;background:radial-gradient(ellipse at 72% 40%,#b58e7e 0 9%,#2a3b8a 24%,#141e6a 55%,#0b1248 100%)}
.hero-title{left:13px;top:122px;font-size:12px;font-weight:800;color:var(--white);letter-spacing:.1px}
.hero-title em{font-style:normal;color:var(--yellow)}
.hero-text{left:13px;top:142px;width:215px;font-size:5px;line-height:10px;color:var(--white)}
.btn-yellow{background:var(--yellow);color:var(--ink);font-size:4.6px;display:flex;align-items:center;justify-content:center}
.hero-btn{left:13px;top:188px;width:45px;height:16px}
.slider-dots{left:318px;top:195px;display:flex;gap:3px}
.slider-dots span{width:8px;height:8px;border-radius:50%;border:1px solid var(--yellow)}
.slider-dots span:first-child{border-color:#c9cbd6}

/* nav */
.main-nav{left:0;top:252px;width:364px;height:26px;background:var(--yellow)}
.nav-item{top:10px;font-size:4.2px;font-weight:700;color:var(--white)}
.nav-item.active{color:var(--navy)}
.nav-underline{left:48px;top:24px;width:54px;height:1.5px;background:var(--navy)}

/* tiles */
.tile{overflow:visible}
.tile-photo{position:absolute;inset:0}
.date-badge{position:absolute;left:2px;top:-8px;width:16px;height:14px;background:var(--white);text-align:center;color:var(--navy);font-weight:800;font-size:6px;line-height:6px;padding-top:2px}
.date-badge small{display:block;font-size:3px;line-height:3px}
.tile-label{position:absolute;left:22px;top:3px;font-size:4.4px;font-weight:700;color:var(--white)}
.caption{position:absolute;left:0;right:0;bottom:0;height:14px;background:var(--caption);display:flex;align-items:center;justify-content:space-between;padding:0 5px 0 3px;font-size:5.6px;font-weight:700;color:var(--navy)}
.caption.big{height:16px;font-size:6.8px;padding-left:5px}
.tick{width:8px;height:8px;border-radius:50%;background:var(--navy);display:flex;align-items:center;justify-content:center}
.tick svg{width:5px;height:5px}
.story-card{background:var(--navy);color:var(--white)}
.story-card h3{position:absolute;left:5px;top:15px;font-size:5.6px;font-weight:700;color:var(--yellow)}
.story-card p{position:absolute;left:5px;top:24px;width:94px;font-size:3.9px;line-height:6.8px}
.story-card .card-foot{position:absolute;left:5px;right:5px;bottom:4px;display:flex;justify-content:space-between;align-items:center;font-size:4.4px;font-weight:700}
.story-card .tick{background:var(--yellow)}

/* newsletter */
.newsletter{left:0;top:547px;width:364px;height:131px;background:linear-gradient(180deg,#2a2623 0%,#3a2e27 45%,#17130f 100%)}
.news-title{left:0;width:364px;top:42px;text-align:center;font-size:12px;font-weight:800;color:var(--white)}
.news-title em{font-style:normal;color:var(--yellow)}
.news-text{left:0;width:364px;top:60px;text-align:center;font-size:5px;line-height:10px;color:var(--white)}
.field{font-size:4.6px;display:flex;align-items:center;padding-left:6px}
.f-email{left:90px;top:81px;width:88px;height:15px;background:var(--yellow);color:var(--ink)}
.f-freq{left:180px;top:81px;width:46px;height:15px;background:var(--yellow);color:var(--ink);justify-content:center;padding:0}
.f-submit{left:228px;top:81px;width:46px;height:15px;background:var(--white);color:var(--ink);justify-content:center;padding:0}

/* contact */
.contact{left:0;top:920px;width:364px;height:141px;background:var(--grey-bg)}
.col-title{top:18px;font-size:5.2px;font-weight:600;color:#333}
.pop-item{left:16px;width:80px;display:flex;gap:3px}
.pop-thumb{width:22px;height:18px;background:linear-gradient(#3b3b3b,#1d1d1d)}
.pop-text{font-size:3.4px;line-height:4.2px;color:#222}
.pop-meta{font-size:2.8px;color:#777;margin-top:1px}
.pop-btn{left:16px;top:104px;width:37px;height:10px}
.input{background:var(--white);border:1px solid #dedede;font-size:3.4px;color:#aaa;display:flex;align-items:center;justify-content:center}
.send-btn{left:102px;top:94px;width:160px;height:17px;font-size:4px;font-weight:600}
.sq{width:22px;height:22px}

/* footer */
.site-footer{left:0;top:1061px;width:364px;height:40px;background:var(--navy)}
.foot-item{top:17px;display:flex;align-items:center;gap:5px;font-size:4px;color:var(--white)}
.foot-item svg{width:8px;height:9px}
.foot-bar{left:0;top:1101px;width:364px;height:19px;background:var(--navy-deep);text-align:center;font-size:3.4px;line-height:19px;color:#9aa6bd}
.foot-bar b{color:var(--white)}
</style>
</head>
<body>
<div class="page">

  <header class="site-header abs">
    <div class="social-dots abs"><span></span><span></span><span></span><span></span></div>
    <div class="brand abs">BRISKET LANTERN</div>
    <div class="menu-icon abs"><i></i><i></i><i></i></div>
  </header>

  <section class="hero abs" role="img" aria-label="Lead story photograph: a speaker at a podium against blurred city lights"></section>
  <h1 class="hero-title abs">YOUR HEADING <em>GOES HERE</em></h1>
  <p class="hero-text abs">Lorem Ipsum is simply dummy text of the printing and typesetting industry. Lorem Ipsum has been the industry's standard dummy text ever since the 1500s, when an unknown printer took a galley of type and scrambled it to make a type specimen book.</p>
  <a class="hero-btn btn-yellow abs">Read more</a>
  <div class="slider-dots abs"><span></span><span></span><span></span></div>

  <nav class="main-nav abs">
    <span class="nav-item active abs" style="left:53px">YOUR NAVIGATION</span>
    <span class="nav-item abs" style="left:125px">YOUR NAVIGATION</span>
    <span class="nav-item abs" style="left:197px">YOUR NAVIGATION</span>
    <span class="nav-item abs" style="left:269px">YOUR NAVIGATION</span>
    <span class="nav-underline abs"></span>
  </nav>

  <!-- first tile group -->
  <article class="tile abs" style="left:13px;top:292px;width:221px;height:154px">
    <div class="tile-photo" role="img" aria-label="Photograph of a cargo ship beached on a hazy shore" style="background:linear-gradient(180deg,#9ea3b3 0%,#b0abaa 60%,#8c7a70 100%)"></div>
    <div class="date-badge">02<small>MAY</small></div>
    <span class="tile-label">Your Heading</span>
    <div class="caption big">Your Heading Goes<span class="tick"><svg viewBox="0 0 10 10"><path d="M2 5.2l2 2 4-4.4" fill="none" stroke="#fff" stroke-width="1.6"/></svg></span></div>
  </article>

  <article class="tile story-card abs" style="left:241px;top:292px;width:107px;height:72px">
    <div class="date-badge">02<small>MAY</small></div>
    <h3>Your Heading Goes Here</h3>
    <p>Lorem Ipsum is simply dummy text of the printing and typesetting industry. Lorem Ipsum has been the industry's standard dummy text ever since the 1500s.</p>
    <div class="card-foot">Your Heading<span class="tick"><svg viewBox="0 0 10 10"><path d="M2 5.2l2 2 4-4.4" fill="none" stroke="#0b2a5b" stroke-width="1.6"/></svg></span></div>
  </article>

  <article class="tile abs" style="left:241px;top:375px;width:107px;height:71px">
    <div class="tile-photo" role="img" aria-label="Photograph of a worker in a dim, lamp-lit workshop" style="background:linear-gradient(135deg,#3a2418,#6b4a35 50%,#1e130d)"></div>
    <div class="date-badge">02<small>MAY</small></div>
    <span class="tile-label">Your Heading</span>
    <div class="caption">Your Heading<span class="tick"><svg viewBox="0 0 10 10"><path d="M2 5.2l2 2 4-4.4" fill="none" stroke="#fff" stroke-width="1.6"/></svg></span></div>
  </article>

  <article class="tile abs" style="left:13px;top:459px;width:107px;height:71px">
    <div class="tile-photo" role="img" aria-label="Photograph of a whale breaching the sea" style="background:linear-gradient(180deg,#5f8fcf,#9ab9e0 60%,#d6e3f2)"></div>
    <div class="date-badge">02<small>MAY</small></div>
    <span class="tile-label">Your Heading</span>
    <div class="caption">Your Heading<span class="tick"><svg viewBox="0 0 10 10"><path d="M2 5.2l2 2 4-4.4" fill="none" stroke="#fff" stroke-width="1.6"/></svg></span></div>
  </article>

  <article class="tile abs" style="left:126px;top:459px;width:107px;height:71px">
    <div class="tile-photo" role="img" aria-label="Photograph of a figure walking through a smoky, firelit street" style="background:radial-gradient(circle at 50% 55%,#d78a3a,#4a3526 45%,#1c1a1a)"></div>
    <div class="date-badge">02<small>MAY</small></div>
    <span class="tile-label">Your Heading</span>
    <div class="caption">Your Heading<span class="tick"><svg viewBox="0 0 10 10"><path d="M2 5.2l2 2 4-4.4" fill="none" stroke="#fff" stroke-width="1.6"/></svg></span></div>
  </article>

  <article class="tile abs" style="left:241px;top:459px;width:107px;height:71px">
    <div class="tile-photo" role="img" aria-label="Photograph of a camel herd in golden dust" style="background:linear-gradient(180deg,#8a6a2e,#c49a4a 50%,#4f3a1d)"></div>
    <div class="date-badge">02<small>MAY</small></div>
    <span class="tile-label">Your Heading</span>
    <div class="caption">Your Heading<span class="tick"><svg viewBox="0 0 10 10"><path d="M2 5.2l2 2 4-4.4" fill="none" stroke="#fff" stroke-width="1.6"/></svg></span></div>
  </article>

  <!-- newsletter -->
  <section class="newsletter abs" role="img" aria-label="Dark harbour scene with a ship at dusk">
    <h2 class="news-title abs">YOUR HEADING <em>GOES HERE</em></h2>
    <p class="news-text abs">Lorem Ipsum is simply dummy text of the printing and typesetting industry.<br>Lorem Ipsum has been the industry's standard dummy text ever since the 1500s.</p>
    <div class="field f-email abs">Your Email</div>
    <div class="field f-freq abs">Daily &#8964;</div>
    <div class="field f-submit abs">Submit</div>
  </section>

  <!-- second tile group -->
  <article class="tile abs" style="left:13px;top:698px;width:107px;height:72px">
    <div class="tile-photo" role="img" aria-label="Photograph of rolled newspapers" style="background:linear-gradient(135deg,#e6e6e6,#9a9a9a 50%,#d8d8d8)"></div>
    <div class="date-badge">01<small>MAY</small></div>
    <div class="caption">Your Heading<span class="tick"><svg viewBox="0 0 10 10"><path d="M2 5.2l2 2 4-4.4" fill="none" stroke="#fff" stroke-width="1.6"/></svg></span></div>
  </article>

  <article class="tile abs" style="left:126px;top:698px;width:107px;height:72px">
    <div class="tile-photo" role="img" aria-label="Photograph of two news anchors in a studio" style="background:linear-gradient(180deg,#1b2f6e,#3a4f94 45%,#c9c9d2)"></div>
    <div class="date-badge">01<small>MAY</small></div>
    <div class="caption">Your Heading<span class="tick"><svg viewBox="0 0 10 10"><path d="M2 5.2l2 2 4-4.4" fill="none" stroke="#fff" stroke-width="1.6"/></svg></span></div>
  </article>

  <article class="tile abs" style="left:241px;top:698px;width:107px;height:72px">
    <div class="tile-photo" role="img" aria-label="Photograph of a presenter in front of a blue screen wall" style="background:linear-gradient(135deg,#1c3a8c,#0e1f55 55%,#2b4aa8)"></div>
    <div class="date-badge">01<small>MAY</small></div>
    <div class="caption">Your Heading<span class="tick"><svg viewBox="0 0 10 10"><path d="M2 5.2l2 2 4-4.4" fill="none" stroke="#fff" stroke-width="1.6"/></svg></span></div>
  </article>

  <article class="tile abs" style="left:13px;top:784px;width:221px;height:120px">
    <div class="tile-photo" role="img" aria-label="Photograph of a costumed performer on a crowded train" style="background:linear-gradient(90deg,#1f4a7a,#5a6f86 45%,#b04a5a 75%,#2c3f6a)"></div>
    <div class="date-badge">01<small>MAY</small></div>
    <div class="caption big">Your Heading Goes<span class="tick"><svg viewBox="0 0 10 10"><path d="M2 5.2l2 2 4-4.4" fill="none" stroke="#fff" stroke-width="1.6"/></svg></span></div>
  </article>

  <article class="tile story-card abs" style="left:241px;top:784px;width:107px;height:120px">
    <div class="date-badge">01<small>MAY</small></div>
    <h3>Your Heading Goes Here</h3>
    <p>Lorem Ipsum is simply dummy text of the printing and typesetting industry. Lorem Ipsum has been the industry's standard dummy text ever since the 1500s, when an unknown printer took a galley of type and scrambled it to make a type specimen book. It has survived not only five centuries, but also the leap into electronic typesetting, remaining essentially unchanged.</p>
    <div class="card-foot">Your Heading<span class="tick"><svg viewBox="0 0 10 10"><path d="M2 5.2l2 2 4-4.4" fill="none" stroke="#0b2a5b" stroke-width="1.6"/></svg></span></div>
  </article>

  <!-- contact -->
  <section class="contact abs">
    <h4 class="col-title abs" style="left:15px">Popular Stories</h4>
    <h4 class="col-title abs" style="left:102px;width:160px;text-align:center">Get In Touch With Us</h4>
    <h4 class="col-title abs" style="left:274px;width:74px;text-align:center">Social Media</h4>

    <div class="pop-item abs" style="top:32px"><div class="pop-thumb" role="img" aria-label="Portrait thumbnail"></div><div class="pop-text"><b>Lorem Ipsum</b> is simply dummy text of the printing and typesetting industry.<div class="pop-meta">admin · 1 day ago</div></div></div>
    <div class="pop-item abs" style="top:56px"><div class="pop-thumb" role="img" aria-label="Portrait thumbnail"></div><div class="pop-text"><b>Lorem Ipsum</b> is simply dummy text of the printing and typesetting industry.<div class="pop-meta">admin · 1 day ago</div></div></div>
    <div class="pop-item abs" style="top:80px"><div class="pop-thumb" role="img" aria-label="Portrait thumbnail"></div><div class="pop-text"><b>Lorem Ipsum</b> is simply dummy text of the printing and typesetting industry.<div class="pop-meta">admin · 1 day ago</div></div></div>
    <a class="pop-btn btn-yellow abs">Read more</a>

    <div class="input abs" style="left:102px;top:32px;width:78px;height:17px">Your Name</div>
    <div class="input abs" style="left:184px;top:32px;width:78px;height:17px">Your Email</div>
    <div class="input abs" style="left:102px;top:53px;width:160px;height:37px">Enter here whatever you want...</div>
    <a class="send-btn btn-yellow abs">SEND THIS MESSAGE NOW</a>

    <span class="sq abs" style="left:274px;top:32px;background:#4aa3df"></span>
    <span class="sq abs" style="left:300px;top:32px;background:#2f4a8a"></span>
    <span class="sq abs" style="left:326px;top:32px;background:#d8322c"></span>
    <span class="sq abs" style="left:274px;top:61px;background:#c8102e"></span>
    <span class="sq abs" style="left:300px;top:61px;background:#1b6fb0"></span>
    <span class="sq abs" style="left:326px;top:61px;background:#e063c4"></span>
    <span class="sq abs" style="left:274px;top:89px;background:#e6892f"></span>
    <span class="sq abs" style="left:300px;top:89px;background:#3b8bd0"></span>
    <span class="sq abs" style="left:326px;top:89px;background:#ff0f7b"></span>
  </section>

  <footer class="site-footer abs">
    <div class="foot-item abs" style="left:74px"><svg viewBox="0 0 10 9"><rect x="0.5" y="1.5" width="9" height="7" fill="#fde425"/><path d="M0.5 1.5l4.5 4 4.5-4" fill="none" stroke="#0b2a5b" stroke-width="0.8"/></svg>info@brisketlantern.co</div>
    <div class="foot-item abs" style="left:158px"><svg viewBox="0 0 10 12"><path d="M5 11.5C2 7.5 1 5.8 1 4.2a4 4 0 018 0c0 1.6-1 3.3-4 7.3z" fill="#fde425"/><circle cx="5" cy="4.2" r="1.5" fill="#0b2a5b"/></svg>Abcdefghijklmnopqrst</div>
    <div class="foot-item abs" style="left:243px"><svg viewBox="0 0 8 12"><rect x="1" y="0.5" width="6" height="11" rx="1" fill="none" stroke="#fde425" stroke-width="1"/><circle cx="4" cy="9.5" r="0.7" fill="#fde425"/></svg>+44 - 0000 - 000000</div>
  </footer>
  <div class="foot-bar abs">© 2016 <b>Brisket Lantern</b>. All rights reserved.</div>

</div>
</body>
</html>
```